Painting Contractor Business Card Design

We are looking for a cool, bold, modern, polished, business card design. We are a high-end residential painting contractor. Please incorporate our logo and keep with our green/black color scheme. We are interested in seeing 2-sided and 1-sided options. Thank you very much!

Industry/Entity Type

Business

Contact Information for Business Card

Info for the card:
Owen Talsky
mobile 206-555-0193
email owen@kestrowfinish.net
web www.kestrowfinish.net

```html
<!DOCTYPE html>
<html lang="en">
<head>
<meta charset="utf-8">
<title>Kestrow Finish – Business Card</title>
<link rel="stylesheet" href="https://fonts.googleapis.com/css2?family=Montserrat:wght@700;800&family=Questrial&display=swap">
<style>
  :root {
    --page-bg: #e6e6e4;
    --card-bg: #ffffff;
    --ink: #111111;
    --brand-green: #2aa847;
    --icon-green: #2fa84a;
    --grad-navy: #1b4a8c;
    --grad-blue: #2082cc;
    --grad-teal: #37b77a;
    --grad-lime: #8cc63f;
    --grad-yellow: #f7c326;
  }
  * { margin: 0; padding: 0; box-sizing: border-box; }
  html, body {
    width: 1200px;
    height: 1000px;
    overflow: hidden;
    background: var(--page-bg);
  }
  .canvas {
    position: relative;
    width: 1200px;
    height: 1000px;
  }
  .card {
    position: absolute;
    left: 250px;
    width: 700px;
    height: 400px;
    background: var(--card-bg);
    box-shadow: 0 6px 20px rgba(0,0,0,0.12);
    overflow: hidden;
  }
  .card--front { top: 70px; }
  .card--back  { top: 530px; }

  /* Front */
  .wordmark {
    position: absolute;
    left: 0; right: 0;
    top: 168px;
    display: flex;
    align-items: center;
    justify-content: center;
    gap: 14px;
  }
  .wordmark__mark {
    width: 26px;
    height: 26px;
    background: var(--brand-green);
  }
  .wordmark__name {
    font-family: "Montserrat", sans-serif;
    font-weight: 800;
    font-size: 34px;
    letter-spacing: 1px;
    color: var(--ink);
  }

  /* Back */
  .person {
    position: absolute;
    left: 62px;
    top: 82px;
  }
  .person__name {
    font-family: "Montserrat", sans-serif;
    font-weight: 800;
    font-size: 40px;
    letter-spacing: 2px;
    color: var(--ink);
    line-height: 1;
  }
  .person__role {
    margin-top: 8px;
    font-family: "Questrial", sans-serif;
    font-size: 21px;
    letter-spacing: 1.5px;
    color: var(--brand-green);
  }
  .contacts {
    position: absolute;
    left: 62px;
    top: 262px;
    list-style: none;
  }
  .contacts__item {
    display: flex;
    align-items: center;
    gap: 14px;
    height: 26px;
    margin-bottom: 4px;
    font-family: "Questrial", sans-serif;
    font-size: 17px;
    color: var(--ink);
  }
  .contacts__icon {
    width: 22px;
    height: 22px;
    border-radius: 3px;
    background: var(--icon-green);
    display: flex;
    align-items: center;
    justify-content: center;
  }
  .brand-graphic {
    position: absolute;
    left: 430px;
    top: 0;
    width: 270px;
    height: 400px;
    background: linear-gradient(200deg,
      var(--grad-yellow) 0%,
      var(--grad-lime) 30%,
      var(--grad-teal) 55%,
      var(--grad-blue) 80%,
      var(--grad-navy) 100%);
  }
</style>
</head>
<body>
<main class="canvas">
  <section class="card card--front" aria-label="Card front">
    <div class="wordmark">
      <span class="wordmark__mark"></span>
      <span class="wordmark__name">KESTROW FINISH</span>
    </div>
  </section>

  <section class="card card--back" aria-label="Card back">
    <div class="person">
      <h1 class="person__name">OWEN TALSKY</h1>
      <p class="person__role">POSITION</p>
    </div>

    <ul class="contacts">
      <li class="contacts__item">
        <span class="contacts__icon">
          <svg width="12" height="14" viewBox="0 0 12 14"><rect x="2" y="1" width="8" height="12" rx="1.5" fill="none" stroke="#fff" stroke-width="1.5"/><circle cx="6" cy="10.5" r="0.9" fill="#fff"/></svg>
        </span>
        206-555-0193
      </li>
      <li class="contacts__item">
        <span class="contacts__icon">
          <svg width="14" height="10" viewBox="0 0 14 10"><rect x="1" y="1" width="12" height="8" fill="none" stroke="#fff" stroke-width="1.4"/><path d="M1 1 L7 6 L13 1" fill="none" stroke="#fff" stroke-width="1.4"/></svg>
        </span>
        owen@kestrowfinish.net
      </li>
      <li class="contacts__item">
        <span class="contacts__icon">
          <svg width="14" height="14" viewBox="0 0 14 14"><circle cx="7" cy="7" r="5.5" fill="none" stroke="#fff" stroke-width="1.3"/><ellipse cx="7" cy="7" rx="2.4" ry="5.5" fill="none" stroke="#fff" stroke-width="1.1"/><path d="M1.5 7 H12.5" stroke="#fff" stroke-width="1.1"/></svg>
        </span>
        www.kestrowfinish.net
      </li>
    </ul>

    <div class="brand-graphic" role="img" aria-label="Large multicolour brand graphic in blue, green and yellow"></div>
  </section>
</main>
</body>
</html>
```